Kereru Creative Food Fiesta

We are holding our inaugural event on the 21st October 2022 on the FieldSolve campus in Palmerston North., from 10am until 2pm.The event will be a mix of Fourth year Food Technology students presenting their student projects and local producers show casing and educating around their products. The event is bought to you by CropNest along with Tarrowby Vale District Council and RIVO. The overall plan is to bring a spotlight to the amount of research and food related businesses are on this side of the river. The event will be free to enter and there will be food and products to purchase, but the main focus is on education.

```html
<!DOCTYPE html>
<html lang="en">
<head>
<meta charset="utf-8">
<title>Kereru Creative Food Fiesta</title>
<link rel="stylesheet" href="https://fonts.googleapis.com/css2?family=Montserrat:wght@500;600;700;800&family=Kaushan+Script&family=Cinzel:wght@500;600&display=swap">
<style>
  :root {
    --backdrop: #f6c441;
    --paper: #f4f4f2;
    --ink: #1d1d1d;
    --festival-red: #d4231c;
    --band-green: #7cb342;
    --pill-gold: #f6b625;
    --pill-ink: #2a2a2a;
    --footer-red: #d42a1f;
    --white: #ffffff;
    --partner-ink: #2b2b2b;
  }
  * { box-sizing: border-box; margin: 0; padding: 0; }
  html, body { width: 1075px; height: 1200px; overflow: hidden; }
  body { background: var(--backdrop); position: relative; font-family: "Montserrat", sans-serif; }

  .poster {
    position: absolute; left: 137px; top: 35px; width: 800px; height: 1130px;
    background: var(--paper); overflow: hidden;
    box-shadow: 0 8px 22px rgba(0,0,0,.25);
  }

  .venue {
    position: absolute; top: 22px; width: 100%; text-align: center;
    font-family: "Cinzel", serif; font-weight: 600; font-size: 21px; letter-spacing: 1px; color: var(--ink);
  }
  .year {
    position: absolute; top: 60px; width: 100%; text-align: center;
    font-weight: 700; font-size: 30px; color: var(--ink);
  }
  .date {
    position: absolute; top: 96px; left: 195px; width: 410px; height: 50px;
    display: flex; align-items: center; justify-content: center; gap: 8px;
    font-weight: 700; color: var(--ink);
  }
  .date::before, .date::after {
    content: ""; position: absolute; left: 0; right: 0; height: 2px; background: var(--ink);
  }
  .date::before { top: 2px; }
  .date::after { bottom: 2px; }
  .date .month, .date .weekday { font-size: 29px; }
  .date .day { font-size: 50px; font-weight: 800; line-height: 1; }

  .event-lead {
    position: absolute; top: 168px; width: 100%; text-align: center;
    font-weight: 500; font-size: 42px; color: var(--ink);
  }
  .event-title {
    position: absolute; top: 222px; width: 100%; text-align: center;
    font-family: "Kaushan Script", cursive; font-size: 110px; line-height: 1.1; color: var(--festival-red);
  }

  .exhibition-band {
    position: absolute; top: 378px; left: 57px; width: 680px; height: 46px;
  }
  .exhibition-band svg { position: absolute; inset: 0; }
  .exhibition-band span {
    position: relative; display: block; line-height: 46px; text-align: center;
    font-family: "Cinzel", serif; font-weight: 600; font-size: 25px; letter-spacing: 1px; color: var(--white);
  }

  .landscape-photo {
    position: absolute; left: 0; top: 430px; width: 100%; height: 545px;
    background: linear-gradient(180deg, #c9d3cf 0%, #6f8f5a 22%, #3f6b35 45%, #2e4f6d 65%, #3b5f82 82%, #5d6b4e 100%);
  }
  .people-photo {
    position: absolute; left: 72px; top: 445px; width: 241px; height: 241px; border-radius: 26px;
    background: linear-gradient(160deg, #9cc7ea 0%, #d9c2ad 50%, #6a7e95 100%);
  }
  .produce-photo {
    position: absolute; left: 472px; top: 714px; width: 235px; height: 241px; border-radius: 26px;
    background: linear-gradient(150deg, #c9ccd0 0%, #eae4d8 50%, #b7b3ab 100%);
  }

  .highlights { position: absolute; left: 339px; top: 446px; width: 389px; list-style: none; }
  .highlights li {
    height: 50px; margin-bottom: 12px; padding: 5px 0 0 30px; border-radius: 25px;
    background: var(--pill-gold); box-shadow: 0 3px 5px rgba(0,0,0,.22);
    font-family: "Cinzel", serif; font-weight: 600; font-size: 16px; line-height: 20px; color: var(--pill-ink);
  }

  .free-entry {
    position: absolute; left: 180px; top: 765px; width: 260px; text-align: center;
    font-weight: 600; font-size: 19px; line-height: 30px; letter-spacing: 6px; color: var(--white);
  }

  .partners {
    position: absolute; left: 0; top: 975px; width: 100%; height: 99px; background: var(--white);
    border-top: 6px solid var(--footer-red);
    display: flex; align-items: center; justify-content: space-around; padding: 0 60px;
  }
  .partner {
    display: flex; align-items: center; gap: 10px;
    font-weight: 700; font-size: 24px; color: var(--partner-ink); white-space: nowrap;
  }
  .partner::before {
    content: ""; width: 14px; height: 14px; background: var(--partner-ink);
  }

  .footer {
    position: absolute; left: 0; top: 1074px; width: 100%; height: 56px; background: var(--footer-red);
    display: flex; align-items: center; justify-content: space-between; padding: 0 40px;
  }
  .site { font-family: "Cinzel", serif; font-weight: 600; font-size: 17px; letter-spacing: 1px; color: var(--white); }
  .social { display: flex; gap: 14px; }
  .social span { width: 24px; height: 24px; border-radius: 50%; background: var(--white); }
</style>
</head>
<body>
<main class="poster">
  <p class="venue">the FieldSolve campus in Palmerston North</p>
  <p class="year">2022</p>
  <p class="date"><span class="month">OCTOBER</span><span class="day">21</span><span class="weekday">FRIDAY</span></p>

  <h1>
    <span class="event-lead">Kereru Creative</span>
    <span class="event-title">Food Fiesta</span>
  </h1>

  <div class="exhibition-band">
    <svg viewBox="0 0 680 46" preserveAspectRatio="none" aria-hidden="true">
      <path d="M6 12 L660 4 L676 20 L664 40 L20 44 L0 30 Z" fill="var(--band-green)"/>
    </svg>
    <span>Innovation in Food exhibition</span>
  </div>

  <div class="landscape-photo" role="img" aria-label="Aerial view of a river winding through green farmland with a bridge in the foreground"></div>
  <div class="people-photo" role="img" aria-label="Group of young people in a circle looking down at the camera against a blue sky"></div>
  <div class="produce-photo" role="img" aria-label="Bottles of plant milk with almonds, coconut and grains on a grey surface"></div>

  <ul class="highlights">
    <li>Local producers stalls with<br>tastings to tempt you</li>
    <li>Harrowgate University food tech<br>student projects</li>
    <li>Chef demonstrations forged<br>from producers stalls</li>
    <li>Research site tours<br>and Robots</li>
  </ul>

  <p class="free-entry">ENTRANCE<br>IS FREE<br>OF CHARGE</p>

  <section class="partners" aria-label="Event partners">
    <span class="partner">RIVO</span>
    <span class="partner">CropNest</span>
    <span class="partner">Tarrowby Vale District Council</span>
  </section>

  <footer class="footer">
    <span class="site">WWW.CROPNEST.CO</span>
    <span class="social" aria-hidden="true"><span></span><span></span><span></span></span>
  </footer>
</main>
</body>
</html>
```